Powerpoint Slides for 'Above Clouds | consulting' firm

Hello,

I would like a suite of slides to not be typical of just ANOther deck. My business name is 'Above Clouds | consulting', so I would like to see innovation and creativity translated into the slides.

1. ‘Company/Cover Page’ – should showcase Above Clouds | consulting branding; perhaps with some animation to give the sense of 'above clouds' content.
The company name, Above Clouds | consulting, and tagline - Strategise | Organise | Optimise | Communicate, should appear together on the front and end page. The company name should appear on all other pages
2. Master branded background slide, with suggested font, and ideally with some colour options which could be leveraged in longer presentations to ‘break’ it up
3. Master branded background slide with an option to include bulleted content within some type of e.g. shape/form (not just as bullets against a blank background)
4. Divider slide (possibly leveraging some of the colours in Point 2

I have attached a copy of the logo/layout of my business card. The square used is raised on the business card which gives a very subtle effect of literally being above clouds. I would like something of a similar feel, but with colour (as noted in Point 2), though very open to ideas/suggestions.

Many Thanks,
Brenda
Updates

This project has been re-opened to all designers. I look forward to seeing creative and innovative submissions. Best Regards, Brenda

Target Market(s)

SMEs and Corporates - however, I don't want to look like just any other consultancy company.

Industry/Entity Type

Business

Colors

Designer to choose colors to be used in the design.

Requirements
Must have
• Innovation; Creativity; Professionalism; Succinct

```html
<!DOCTYPE html>
<html lang="en">
<head>
<meta charset="utf-8">
<title>Above Clouds | consulting – slide suite</title>
<link href="https://fonts.googleapis.com/css2?family=Questrial&family=Montserrat:wght@700&family=Arimo:wght@400;700&family=EB+Garamond:wght@400&display=swap" rel="stylesheet">
<style>
  :root{
    --stage:#000;
    --white:#fff;
    --charcoal:#3f3f3f;
    --number:#5b5b5b;
    --mist:#d6d6d6;
    --mist-light:#e3e3e3;
    --frame:#9b9b9b;
    --frame-light:#c9c9c9;
    --blue:#4a7ebb;
    --green:#77933c;
    --ink:#1e1e1e;
    --ink-soft:#333;
    --grey-text:#7a7a7a;
    --thin:"Questrial", sans-serif;
    --head:"Montserrat", sans-serif;
    --sans:"Arimo", sans-serif;
    --serif:"EB Garamond", serif;
  }
  *{box-sizing:border-box;margin:0;padding:0}
  html,body{width:1200px;height:996px;overflow:hidden;background:var(--stage)}
  .canvas{position:relative;width:1200px;height:996px}
  .slide{position:absolute;overflow:hidden;background:var(--white)}
  .slide--cover{left:15px;top:0;width:581px;height:324px}
  .slide--section{left:607px;top:0;width:578px;height:324px;background:var(--mist)}
  .slide--team{left:15px;top:334px;width:581px;height:327px}
  .slide--services{left:607px;top:334px;width:578px;height:327px}
  .slide--promise{left:15px;top:672px;width:581px;height:324px}
  .slide--bullets{left:607px;top:672px;width:578px;height:324px}
  .abs{position:absolute}

  /* cover */
  .cover__name{left:0;top:112px;width:581px;text-align:center;font-family:var(--thin);font-size:28px;color:#555;line-height:36px}
  .cover__tagline{left:0;top:235px;width:581px;text-align:center;font-family:var(--thin);font-size:7.5px;letter-spacing:2.6px;color:#666}
  .cover__band{left:0;top:277px;width:581px;height:47px;background:var(--mist-light)}
  .cover__by{right:158px;top:286px;font-family:var(--thin);font-size:14px;color:var(--grey-text)}
  .cover__rule{left:445px;top:282px;width:1px;height:37px;background:#888}
  .cover__presenter{left:469px;top:283px;font-family:var(--thin);font-size:14px;font-weight:bold;color:var(--grey-text)}
  .cover__date{left:469px;top:301px;font-family:var(--thin);font-size:11px;color:var(--grey-text)}

  /* section */
  .section__band{left:0;top:133px;width:578px;height:63px;background:var(--charcoal)}
  .section__frame{left:25px;top:108px;width:72px;height:82px;border:9px solid var(--frame)}
  .section__square{left:47px;top:94px;width:77px;height:76px;background:var(--blue)}
  .section__title{left:130px;top:132px;font-family:var(--thin);font-size:50px;font-weight:normal;color:var(--white);line-height:62px}
  .section__subtitle{left:130px;top:196px;font-family:var(--thin);font-size:26px;font-weight:normal;color:var(--ink);text-shadow:2px 3px 3px rgba(0,0,0,.35)}

  /* footer name plate */
  .plate{left:50%;transform:translateX(-50%);bottom:6px;width:100px;height:38px;background:var(--mist-light);display:flex;align-items:center;justify-content:center}
  .slide--section .plate{background:transparent}
  .plate__name{font-family:var(--thin);font-size:7px;color:var(--white)}

  /* header bar */
  .header{left:0;top:12px;width:100%;height:30px;background:var(--charcoal)}
  .header__frame{left:13px;top:19px;width:33px;height:33px;border:5px solid var(--frame)}
  .header__square{left:24px;top:7px;width:31px;height:35px;background:var(--mist)}
  .header__square--blue{background:var(--blue)}
  .header__square--green{background:var(--green)}
  .header__title{left:73px;top:12px;line-height:30px;font-family:var(--head);font-size:19px;color:var(--white);letter-spacing:.5px}
  .header__page{right:18px;top:4px;width:31px;height:27px;background:var(--number);color:var(--white);font-family:var(--sans);font-size:10px;font-weight:bold;display:flex;align-items:center;justify-content:center}

  /* team */
  .member{position:absolute;top:0;width:170px;height:327px}
  .member__frame{left:0;top:52px;width:70px;height:82px;border:6px solid var(--frame-light);border-right:none}
  .member__photo{left:20px;top:61px;width:92px;height:88px;background:linear-gradient(135deg,#cdb7a6,#8a6d5c 55%,#e9e2dc)}
  .member__photo--b{background:linear-gradient(135deg,#e6e3de,#b06a4e 55%,#f1efec)}
  .member__photo--c{background:linear-gradient(135deg,#f2f2f2,#9f8a7d 55%,#4b4b52)}
  .member__name{left:0;top:167px;font-family:var(--sans);font-weight:bold;font-size:12px;color:var(--blue)}
  .member__role{left:0;top:181px;font-family:var(--serif);font-weight:bold;font-size:11px;color:var(--ink)}
  .member__bio{left:17px;top:197px;width:122px;font-family:var(--serif);font-size:10.5px;line-height:14.5px;color:var(--ink-soft)}

  /* services */
  .services__band{left:0;top:42px;width:578px;height:55px;background:var(--mist)}
  .service{position:absolute;width:140px}
  .service__card{left:0;top:0;width:66px;height:58px;background:var(--white);padding:8px;display:flex}
  .service__icon{width:50px;height:42px;background:var(--mist-light);display:flex;align-items:center;justify-content:center}
  .service__heading{left:0;font-family:var(--sans);font-weight:bold;font-size:13.5px;color:var(--ink);white-space:nowrap}
  .service__text{left:0;width:130px;font-family:var(--serif);font-size:10.5px;line-height:15px;color:var(--ink-soft)}

  /* promise */
  .promise__image{left:0;top:42px;width:275px;height:282px;background:radial-gradient(circle at 55% 40%,#d8d8d8,#8d8d8d 45%,#3a3a3a)}
  .promise__badge{left:9px;top:221px;width:122px;height:87px;background:rgba(74,126,187,.92);color:var(--ink);font-family:var(--sans);font-size:13px;line-height:17px;text-align:center;display:flex;align-items:center;justify-content:center}
  .promise__title{left:297px;top:62px;font-family:var(--thin);font-size:20px;font-weight:normal;color:var(--ink)}
  .promise__copy{left:297px;top:95px;width:268px;font-family:var(--serif);font-size:11px;line-height:16px;color:var(--ink-soft)}
  .promise__copy p{margin-bottom:8px}

  /* bullets */
  .bullets__column{left:0;top:42px;width:146px;height:282px;background:var(--mist-light)}
  .bullets__panel{left:40px;top:69px;width:437px;height:44px;background:var(--white)}
  .bullets__heading{left:46px;top:72px;width:425px;height:38px;background:var(--mist);font-family:var(--sans);font-weight:bold;font-size:17px;color:var(--ink);padding-left:10px;line-height:38px}
  .bullets__list{left:185px;top:124px;width:345px;font-family:var(--serif);font-size:12.5px;line-height:18px;color:var(--ink-soft);list-style:disc}
  .bullets__list li{margin-bottom:11px}
</style>
</head>
<body>
<main class="canvas">

  <section class="slide slide--cover" aria-label="Cover slide">
    <p class="abs cover__name">Above Clouds | consulting</p>
    <p class="abs cover__tagline">STRATEGISE | ORGANISE | OPTIMISE | COMMUNICATE</p>
    <div class="abs cover__band"></div>
    <p class="abs cover__by">Presented by</p>
    <div class="abs cover__rule"></div>
    <p class="abs cover__presenter">Helen Marsh</p>
    <p class="abs cover__date">19<sup>th</sup> August 2014</p>
  </section>

  <section class="slide slide--section" aria-label="Section divider slide">
    <div class="abs section__band"></div>
    <div class="abs section__frame"></div>
    <div class="abs section__square"></div>
    <h1 class="abs section__title">Section Title</h1>
    <h2 class="abs section__subtitle">Subtitle heading</h2>
    <div class="abs plate"><span class="plate__name">Above Clouds</span></div>
  </section>

  <section class="slide slide--team" aria-label="Team slide">
    <div class="abs header"></div>
    <div class="abs header__frame"></div>
    <div class="abs header__square"></div>
    <h2 class="abs header__title">MEET OUR TEAM</h2>
    <div class="abs header__page">4</div>

    <article class="member" style="left:34px">
      <div class="abs member__frame"></div>
      <div class="abs member__photo" role="img" aria-label="Portrait photo of Helen Marsh"></div>
      <p class="abs member__name">Helen Marsh</p>
      <p class="abs member__role">Lead Consultant</p>
      <p class="abs member__bio">Consectetuer adipiscing elit. Maecenas porttitor congue massa. Fusce posuere, magna sed pulvinar ultricies.</p>
    </article>
    <article class="member" style="left:223px">
      <div class="abs member__frame"></div>
      <div class="abs member__photo member__photo--b" role="img" aria-label="Portrait photo of Nina Ford"></div>
      <p class="abs member__name">Nina Ford</p>
      <p class="abs member__role">Lead Consultant</p>
      <p class="abs member__bio">Consectetuer adipiscing elit. Maecenas porttitor congue massa. Fusce posuere, magna sed pulvinar ultricies.</p>
    </article>
    <article class="member" style="left:407px">
      <div class="abs member__frame"></div>
      <div class="abs member__photo member__photo--c" role="img" aria-label="Portrait photo of Tom Reyes"></div>
      <p class="abs member__name">Tom Reyes</p>
      <p class="abs member__role">Lead Consultant</p>
      <p class="abs member__bio">Consectetuer adipiscing elit. Maecenas porttitor congue massa. Fusce posuere, magna sed pulvinar ultricies.</p>
    </article>
    <div class="abs plate" style="bottom:8px"><span class="plate__name">Above Clouds</span></div>
  </section>

  <section class="slide slide--services" aria-label="Services slide">
    <div class="abs services__band"></div>
    <div class="abs header"></div>
    <div class="abs header__frame"></div>
    <div class="abs header__square header__square--blue"></div>
    <h2 class="abs header__title">TITLE SLIDE</h2>
    <div class="abs header__page">5</div>

    <article class="service" style="left:36px;top:62px">
      <div class="abs service__card"><div class="service__icon">
        <svg width="26" height="32" viewBox="0 0 26 32" fill="none" stroke="#4a7ebb" stroke-width="1.8"><path d="M13 2a9 9 0 0 0-5 16.5V23h10v-4.5A9 9 0 0 0 13 2z"/><path d="M9 26h8M10 29h6M13 23v-8l-3-3M13 15l3-3"/></svg>
      </div></div>
      <h3 class="abs service__heading" style="top:74px">Lorem ipsum dolor</h3>
      <p class="abs service__text" style="top:92px">Consectetuer adipiscing elit. Maecenas porttitor congue massa. Fusce posuere, magna sed pulvinar ultricies, purus lectus malesuada libero, sit amet commodo magna eros quis?</p>
    </article>
    <article class="service" style="left:231px;top:62px">
      <div class="abs service__card"><div class="service__icon">
        <svg width="26" height="30" viewBox="0 0 26 30" fill="none" stroke="#4a7ebb" stroke-width="1.8"><rect x="6" y="4" width="14" height="16"/><rect x="3" y="22" width="20" height="5"/></svg>
      </div></div>
      <h3 class="abs service__heading" style="top:66px">Lorem ipsum dolor</h3>
      <p class="abs service__text" style="top:84px">Consectetuer adipiscing elit. Maecenas porttitor congue massa. Fusce posuere, magna sed pulvinar ultricies, purus lectus malesuada libero, sit amet commodo magna eros quis?</p>
    </article>
    <article class="service" style="left:426px;top:62px">
      <div class="abs service__card"><div class="service__icon">
        <svg width="32" height="28" viewBox="0 0 32 28" fill="none" stroke="#4a7ebb" stroke-width="1.6"><rect x="3" y="18" width="4" height="8"/><rect x="10" y="14" width="4" height="12"/><rect x="17" y="10" width="4" height="16"/><rect x="24" y="6" width="4" height="20"/><path d="M2 14 10 8l6 3 12-9M24 2h4v4"/></svg>
      </div></div>
      <h3 class="abs service__heading" style="top:70px">Lorem ipsum dolor</h3>
      <p class="abs service__text" style="top:88px">Consectetuer adipiscing elit. Maecenas porttitor congue massa. Fusce posuere, magna sed pulvinar ultricies, purus lectus malesuada libero, sit amet commodo magna eros quis?</p>
    </article>
    <div class="abs plate" style="bottom:8px"><span class="plate__name">Above Clouds</span></div>
  </section>

  <section class="slide slide--promise" aria-label="Promise slide">
    <div class="abs promise__image" role="img" aria-label="Black and white photo of a hand touching glowing light bulb sketches"></div>
    <div class="abs header"></div>
    <div class="abs header__frame"></div>
    <div class="abs header__square header__square--blue"></div>
    <h2 class="abs header__title">TITLE SLIDE</h2>
    <div class="abs header__page">6</div>
    <div class="abs promise__badge">Our promise,<br>to you and<br>your business</div>
    <h3 class="abs promise__title">We’re here to look after you.</h3>
    <div class="abs promise__copy">
      <p>Consectetuer adipiscing elit. Maecenas porttitor congue massa. Fusce posuere, magna sed pulvinar ultricies, purus lectus malesuada libero, sit amet commodo magna eros quis urna.</p>
      <p>Nunc viverra imperdiet enim. Fusce est. Vivamus a tellus.</p>
      <p>Pellentesque habitant morbi tristique senectus et netus et malesuada fames ac turpis egestas. Proin pharetra nonummy pede. Mauris et orci.</p>
    </div>
    <div class="abs plate"><span class="plate__name">Above Clouds</span></div>
  </section>

  <section class="slide slide--bullets" aria-label="Bulleted content slide">
    <div class="abs bullets__column"></div>
    <div class="abs header"></div>
    <div class="abs header__frame"></div>
    <div class="abs header__square header__square--green"></div>
    <h2 class="abs header__title">TITLE SLIDE</h2>
    <div class="abs header__page">7</div>
    <div class="abs bullets__panel"></div>
    <h3 class="abs bullets__heading">Lorem ipsum dolor?</h3>
    <ul class="abs bullets__list">
      <li>Consectetuer adipiscing elit. Vivamus a tellus.</li>
      <li>Nunc viverra imperdiet enim. Fusce est.</li>
      <li>Maecenas porttitor congue massa.</li>
      <li>Fusce posuere, magna sed pulvinar ultricies, purus lectus malesuada libero, sit amet commodo magna eros quis?</li>
    </ul>
    <div class="abs plate"><span class="plate__name">Above Clouds</span></div>
  </section>

</main>
</body>
</html>
```